fieldscoutingpath.com - Social Media Branding

fieldscoutingpath.com --> Social Media Re-Branding & Graphics
Facebook: @fldscoutpath - Instagram: @fieldscoutingpath - Twitter: @fldscoutpath

Looking to find a good designer to help with my fieldscoutingpath.com social media sites!
- facebook banner
- twitter banner
- instagram template (square and banner size)
- Quote or Information Template
- Committed Template (uniformed) - see the ones I made (& i am no professional) at fieldscoutingpath.com/committed - needs to have fieldscoutingpath.com logo, room for: the committed school and the team the player plays on.

Also willing to pay extra for a graphic that is the "complete package" that detail all of the steps of the recruiting process detailed in fieldscoutingpath.com

Font styles to use
Sans Serif

Colors
ec1f27
fbee3e

```html
<!DOCTYPE html>
<html lang="en">
<head>
<meta charset="utf-8">
<title>fieldscoutingpath.com – Social Banners</title>
<link rel="stylesheet" href="https://fonts.googleapis.com/css2?family=Jost:wght@400;500;600;700;800&display=swap">
<style>
  :root{
    --stage:#1a1a1a;
    --red:#c8202f;
    --red-bright:#ec1f27;
    --yellow:#f0ef4f;
    --yellow-brand:#fbee3e;
    --ink:#0d0d0d;
    --white:#ffffff;
    --clay:#d9713e;
    --grass:#2f4a22;
  }
  *{box-sizing:border-box;margin:0;padding:0}
  html,body{width:755px;height:1200px;overflow:hidden;background:var(--stage)}
  body{position:relative;font-family:"Jost",sans-serif}
  .banner{position:absolute;overflow:hidden}
  .photo{position:absolute;inset:0}
  .brand{position:absolute;display:flex;align-items:center;gap:6px;font-weight:600;letter-spacing:.2px;white-space:nowrap}
  .brand-dot{border-radius:50%;flex:none}
  .kicker{position:absolute;font-weight:600;white-space:nowrap;letter-spacing:.3px}
  .headline{position:absolute;font-weight:800;white-space:nowrap;letter-spacing:-.5px;line-height:1}
  .cta{position:absolute;display:flex;align-items:center;justify-content:center;border-radius:999px;font-weight:600;letter-spacing:.5px;white-space:nowrap}

  /* Facebook cover – white */
  .cover-white{left:28px;top:28px;width:705px;height:268px;background:var(--white)}
  .cover-white .photo{left:290px;background:
      linear-gradient(90deg,var(--white) 0%,rgba(255,255,255,.6) 12%,rgba(255,255,255,0) 30%),
      linear-gradient(180deg,#27401f 0%,#3b5a2c 38%,#6b7a4c 50%,#cfa27a 62%,#b88460 100%)}
  .cover-white .brand{left:74px;top:64px;font-size:17px;color:#555}
  .cover-white .brand-dot{width:22px;height:22px;background:var(--yellow)}
  .cover-white .kicker{left:74px;top:125px;font-size:20px;color:var(--red)}
  .cover-white .headline{left:72px;top:152px;font-size:41px;color:var(--ink)}
  .cover-white .cta{left:71px;top:221px;width:209px;height:41px;background:var(--yellow);color:var(--white);font-size:20px}

  /* Wide gradient banner */
  .cover-gradient{left:27px;top:313px;width:705px;height:268px}
  .cover-gradient .photo{background:
      linear-gradient(95deg,rgba(190,40,55,.85) 0%,rgba(215,90,70,.75) 50%,rgba(230,180,60,.8) 100%),
      linear-gradient(180deg,#6b4a3a 0%,#9c6a4d 55%,#c96a3c 75%,#d8804a 100%)}
  .cover-gradient .ball{position:absolute;left:463px;top:140px;width:124px;height:124px;border-radius:50%;background:radial-gradient(circle at 40% 35%,#f4e86a,#d9c23a 70%,#b9a030)}
  .cover-gradient .brand{left:0;right:0;justify-content:center;top:360px;font-size:15px;color:var(--white)}
  .cover-gradient .brand-dot{width:18px;height:18px;background:var(--white)}
  .cover-gradient .kicker{left:163px;top:96px;font-size:22px;color:var(--white)}
  .cover-gradient .headline{left:162px;top:127px;font-size:44px;color:var(--white)}
  .cover-gradient .cta{left:270px;top:191px;width:158px;height:30px;border:1.5px solid var(--white);color:var(--white);font-size:15px}

  /* Square gradient */
  .square-gradient{left:27px;top:602px;width:343px;height:273px}
  .square-gradient .photo{background:
      linear-gradient(100deg,rgba(190,40,55,.85) 0%,rgba(215,95,70,.75) 60%,rgba(225,160,70,.8) 100%),
      linear-gradient(180deg,#6b4a3a 0%,#9c6a4d 50%,#c96a3c 70%,#d8804a 100%)}
  .square-gradient .ball{position:absolute;left:236px;top:148px;width:88px;height:88px;border-radius:50%;background:radial-gradient(circle at 40% 35%,#f4e86a,#d9c23a 70%,#b9a030)}
  .square-gradient .brand{left:0;right:0;justify-content:center;top:59px;font-size:11px;color:var(--white)}
  .square-gradient .brand-dot{width:14px;height:14px;background:var(--white)}
  .square-gradient .kicker{left:41px;top:106px;font-size:16.5px;color:var(--white)}
  .square-gradient .headline{left:40px;top:132px;font-size:32px;color:var(--white)}
  .square-gradient .cta{left:107px;top:189px;width:126px;height:24px;border:1.2px solid var(--white);color:var(--white);font-size:12px}

  /* Square white */
  .square-white{left:388px;top:602px;width:343px;height:343px;background:var(--white)}
  .square-white .photo{bottom:auto;height:230px;background:
      linear-gradient(180deg,rgba(255,255,255,0) 55%,var(--white) 100%),
      linear-gradient(180deg,#27401f 0%,#3b5a2c 35%,#6b7a4c 50%,#cfa27a 70%,#b88460 100%)}
  .square-white .brand{left:0;right:0;justify-content:center;top:192px;font-size:12px;color:var(--ink)}
  .square-white .brand-dot{width:15px;height:15px;background:var(--yellow)}
  .square-white .kicker{left:51px;top:233px;font-size:16px;color:var(--red)}
  .square-white .headline{left:50px;top:252px;font-size:30px;color:var(--ink)}
  .square-white .cta{left:111px;top:295px;width:127px;height:25px;background:var(--red);color:var(--white);font-size:12px;box-shadow:0 3px 6px rgba(0,0,0,.2)}

  /* Quote template */
  .quote{left:27px;top:888px;width:343px;height:283px}
  .quote .photo{background:
      linear-gradient(180deg,rgba(200,150,150,.7) 0%,rgba(210,110,80,.5) 55%,rgba(220,120,60,.6) 100%),
      linear-gradient(180deg,#8a7060 0%,#6b7a4c 30%,#c06a3e 70%,#d8804a 100%)}
  .quote-band{position:absolute;left:0;right:0;top:69px;height:148px;background:rgba(200,32,47,.82)}
  .quote .ball{position:absolute;left:231px;top:107px;width:112px;height:112px;border-radius:50%;background:radial-gradient(circle at 40% 35%,#f2f26a,#d8e03a 70%,#b0b52a)}
  .quote-mark{position:absolute;left:93px;top:73px;width:24px;height:22px}
  .quote-text{position:absolute;left:21px;top:110px;width:210px;font-size:10px;line-height:14.5px;color:var(--white);font-weight:400}
  .quote-author{position:absolute;left:149px;top:190px;font-size:10.5px;font-weight:700;color:var(--white);letter-spacing:.3px}
  .quote .brand{left:104px;top:243px;font-size:11px;color:var(--white)}
  .quote .brand-dot{width:16px;height:16px;background:var(--white)}
</style>
</head>
<body>

<section class="banner cover-white">
  <div class="photo" role="img" aria-label="Photo of a softball batter waiting for a pitch while a coach watches from behind"></div>
  <div class="brand"><span class="brand-dot"></span>fieldscoutingpath.com</div>
  <p class="kicker">OVER 2 MILLION DOLLARS IN</p>
  <h1 class="headline">SCHOLARSHIPS</h1>
  <div class="cta">GET STARTED</div>
</section>

<section class="banner cover-gradient">
  <div class="photo" role="img" aria-label="Blurred softball field with a red to yellow colour wash"></div>
  <div class="ball" role="img" aria-label="Softball resting on the infield dirt"></div>
  <div class="brand" style="top:52px"><span class="brand-dot"></span>fieldscoutingpath.com</div>
  <p class="kicker">OVER 2 MILLION DOLLARS IN</p>
  <h2 class="headline">SCHOLARSHIPS</h2>
  <div class="cta">GET STARTED</div>
</section>

<section class="banner square-gradient">
  <div class="photo" role="img" aria-label="Blurred softball field with a red to orange colour wash"></div>
  <div class="ball" role="img" aria-label="Softball resting on the infield dirt"></div>
  <div class="brand"><span class="brand-dot"></span>fieldscoutingpath.com</div>
  <p class="kicker">OVER 2 MILLION DOLLARS IN</p>
  <h2 class="headline">SCHOLARSHIPS</h2>
  <div class="cta">GET STARTED</div>
</section>

<section class="banner square-white">
  <div class="photo" role="img" aria-label="Photo of a softball batter facing a pitcher, fading into white"></div>
  <div class="brand"><span class="brand-dot"></span>fieldscoutingpath.com</div>
  <p class="kicker">OVER 2 MILLION DOLLARS IN</p>
  <h2 class="headline">SCHOLARSHIPS</h2>
  <div class="cta">GET STARTED</div>
</section>

<section class="banner quote">
  <div class="photo" role="img" aria-label="Blurred softball field behind a quote"></div>
  <div class="quote-band"></div>
  <div class="ball" role="img" aria-label="Softball resting on the infield dirt"></div>
  <svg class="quote-mark" viewBox="0 0 24 22" aria-hidden="true">
    <path fill="#fff" d="M1 0h9v10c0 6-3 10-8 12l-1-3c3-1 4-3 4-6H1z M14 0h9v10c0 6-3 10-8 12l-1-3c3-1 4-3 4-6h-4z"/>
  </svg>
  <p class="quote-text">Lorem ipsum dolor sit amet, consectetur adipiscing elit, sed do eiusmod tempor incididunt ut labore et dolore magna aliqua. Quis ipsum suspendisse ultrices gravida. Risus commodo viverra maecenas</p>
  <p class="quote-author">JOHN SMITH</p>
  <div class="brand"><span class="brand-dot"></span>fieldscoutingpath.com</div>
</section>

</body>
</html>
```